Juniper Estates - wanted BRILLIANT website design for our new property investing company

We need a website design for our new company based in Bristol, England, UK called "Juniper Estates". We help buy people property who are in financial difficulty or who are needing to sell their property quickly for reasons such as death, divorce/separation, relocation, emigration.

We have a logo being designed incorporating strawberry and property (so red and green). We would like designs to communicate an elegant ,professional, approachable, friendly
fresh clean but also warm appealing appearance
Not too busy
Website consistent with logo and company name i.e. colour scheme

Please use our word document for content as a guide but use professional judgement for minor alterations if you feel they would benefit the site/structure etc

Please ask at any time if not sure

Target Market(s)

Adult british population, those that have a mortgage / loan / own property

Industry/Entity Type

Financial

Font styles to use
Serif
Sans Serif
Decorative

Colors
0692cd
33b7a4
acd036
fbee3e
3176b5
886aae
a6479a
e567a6
eb1f27

Requirements
Must have
• This must not look like a template website we are looking for UNIQUE please!
Nice to have
• Bristol pictures instead of generic, or colourful line drawings/comic drawings of houses/property/keys/happy people.....
Should not have
• An obvious off the shelf template design

```html
<!DOCTYPE html>
<html lang="en">
<head>
<meta charset="utf-8">
<title>Juniper Estates</title>
<link href="https://fonts.googleapis.com/css2?family=Montserrat:wght@400;500;600;700&family=Open+Sans:wght@400;600&display=swap" rel="stylesheet">
<style>
:root{
  --red:#d1262c;
  --red-dark:#b81d22;
  --green:#7dbb3a;
  --green-dark:#62a127;
  --text:#3a3a3a;
  --muted:#555;
  --beige:#f5f0dc;
  --beige-line:#e2dcc2;
  --navy:#172232;
  --navy-text:#3d5a7c;
  --field:#e6e6e6;
  --white:#fff;
}
*{box-sizing:border-box;margin:0;padding:0}
html,body{width:813px;height:1200px;overflow:hidden;background:var(--white)}
body{font-family:"Open Sans",Arial,sans-serif;color:var(--text);position:relative}
.page{position:relative;width:813px;height:1200px;overflow:hidden}

/* header */
.site-header{position:absolute;top:0;left:0;width:813px;height:80px;background:var(--white)}
.brand{position:absolute;left:96px;top:42px;display:flex;align-items:center;gap:8px}
.brand-dot{width:14px;height:14px;border-radius:50%;background:var(--red)}
.brand-name{font-family:"Montserrat",sans-serif;font-weight:600;font-size:16px;color:var(--red)}
.header-contact{position:absolute;right:96px;top:24px;display:flex;gap:8px;align-items:center}
.header-contact svg{width:26px;height:26px}
.contact-label{font-family:"Montserrat",sans-serif;font-size:10px;letter-spacing:.5px;color:#666;text-transform:uppercase}
.contact-number{font-family:"Montserrat",sans-serif;font-size:18px;font-weight:500;color:#444;letter-spacing:1px;line-height:20px}

/* nav */
.main-nav{position:absolute;top:80px;left:0;width:813px;height:31px;background:linear-gradient(#8fca4a,var(--green-dark))}
.main-nav ul{list-style:none;display:flex;gap:0;position:absolute;left:107px;top:10px}
.main-nav li{font-family:"Montserrat",sans-serif;font-weight:600;font-size:9px;color:var(--white);text-transform:uppercase;margin-right:29px}

/* hero */
.hero{position:absolute;top:111px;left:0;width:813px;height:344px}
.hero-photo{position:absolute;inset:0;background:linear-gradient(180deg,#9ec0dc 0%,#c9d8e4 35%,#e8ebe9 55%,#9aa888 80%,#6f8a55 100%)}
.steps{position:absolute;left:96px;top:39px}
.step{position:absolute;left:0;display:flex;align-items:center;gap:8px;width:220px}
.step-icon{width:44px;height:44px;border-radius:50%;background:var(--white);box-shadow:0 1px 4px rgba(0,0,0,.25);display:flex;align-items:center;justify-content:center}
.step-icon svg{width:20px;height:20px}
.step-label{font-family:"Montserrat",sans-serif;font-weight:600;font-size:8.5px;letter-spacing:1px;color:#222;text-transform:uppercase}
.steps-path{position:absolute;left:200px;top:50px}
.steps-title{position:absolute;left:300px;top:93px;width:94px;text-align:center;font-family:"Montserrat",sans-serif;color:var(--white);text-shadow:0 1px 3px rgba(0,0,0,.35)}
.steps-title .the,.steps-title .easy{font-size:22px;font-weight:500;line-height:24px}
.steps-title .steps-word{font-size:20px;font-weight:600}
.steps-num{width:42px;height:42px;border-radius:50%;background:var(--white);color:var(--red);font-size:24px;font-weight:700;line-height:42px;margin:6px auto 8px;text-shadow:none;box-shadow:0 1px 4px rgba(0,0,0,.3)}

.valuation{position:absolute;left:405px;top:37px;width:313px;height:262px;background:rgba(255,255,255,.9);padding:10px;box-shadow:0 1px 6px rgba(0,0,0,.2)}
.valuation-inner{background:var(--white);height:100%;position:relative}
.valuation-head{height:26px;background:var(--red);display:flex;align-items:center;gap:12px;padding-left:10px;font-family:"Montserrat",sans-serif;font-weight:600;font-size:12.5px;color:var(--white);text-transform:uppercase}
.field{position:absolute;background:var(--field);border-radius:5px;height:24px;font-size:8.5px;color:#888;padding:7px 13px}
.submit{position:absolute;left:12px;top:215px;width:91px;height:25px;background:var(--red);border-radius:3px;color:var(--white);font-family:"Montserrat",sans-serif;font-weight:700;font-size:8.5px;text-align:center;line-height:25px}

/* welcome */
.welcome{position:absolute;top:455px;left:0;width:813px;height:195px}
.welcome h1{position:absolute;left:96px;top:30px;font-family:"Montserrat",sans-serif;font-size:12.5px;font-weight:700;color:#222;text-transform:uppercase}
.welcome h1 span{color:var(--red);margin-left:4px}
.welcome-text{position:absolute;left:96px;top:52px;width:292px;font-size:8.5px;line-height:13.4px;color:var(--muted)}
.welcome-text p+p{margin-top:13px}
.welcome-photo{position:absolute;left:425px;top:32px;width:293px;height:137px;border:6px solid #d5d5d5;background:linear-gradient(135deg,#dfe8ee 0%,#b9c9b0 45%,#6d9e4a 100%)}

/* help */
.help{position:absolute;top:650px;left:0;width:813px;height:134px;background:var(--beige);border-top:1px solid var(--beige-line);border-bottom:1px solid var(--beige-line)}
.section-title{font-family:"Montserrat",sans-serif;font-weight:700;font-size:10.5px;color:#222;text-transform:uppercase;text-align:center;line-height:16px}
.help .section-title{position:absolute;top:22px;width:100%}
.tick-list{position:absolute;list-style:none}
.tick-list li{position:relative;padding-left:13px;font-size:8px;color:var(--muted);height:23px}
.tick-list li::before{content:"";position:absolute;left:0;top:1px;width:3px;height:6px;border:solid var(--green);border-width:0 2px 2px 0;transform:rotate(40deg)}

/* specialize */
.special{position:absolute;top:784px;left:0;width:813px;height:157px;border-bottom:1px solid #e4e4e4}
.special .section-title{position:absolute;top:20px;width:100%}
.special .tick-list li{height:23px;line-height:11px}
.special-rule{position:absolute;left:96px;top:941px;width:622px;height:1px;background:#e4e4e4}

/* badges */
.badges{position:absolute;top:942px;left:0;width:813px;height:108px}
.badge{position:absolute}
.badge-divider{position:absolute;top:10px;width:1px;height:68px;background:#e4e4e4}

/* footer */
.site-footer{position:absolute;top:1050px;left:0;width:813px;height:150px;background:var(--navy);text-align:center}
.footer-brand{position:absolute;top:52px;width:100%;display:flex;justify-content:center;align-items:center;gap:7px}
.footer-brand .brand-dot{background:var(--white)}
.footer-brand .brand-name{color:var(--white);font-size:13px}
.footer-nav{position:absolute;top:79px;width:100%;display:flex;justify-content:center;gap:10px;list-style:none;font-family:"Montserrat",sans-serif;font-size:8px;color:var(--navy-text);text-transform:uppercase}
.social{position:absolute;top:99px;left:385px;display:flex;gap:6px}
.social span{width:19px;height:19px;background:#2a4664;border-radius:2px}
.copyright{position:absolute;top:129px;width:100%;font-size:7px;color:var(--navy-text)}
</style>
</head>
<body>
<div class="page">

  <header class="site-header">
    <div class="brand"><span class="brand-dot"></span><span class="brand-name">Juniper Estates</span></div>
    <div class="header-contact">
      <svg viewBox="0 0 26 26"><path d="M6 3c2 0 3 4 3 5s-2 2-2 3 3 6 6 7c1 0 2-2 3-2s5 1 5 3-2 4-4 4C10 23 3 15 3 8c0-2 1-5 3-5z" fill="#888"/><circle cx="19" cy="7" r="5" fill="none" stroke="#888" stroke-width="1.4"/></svg>
      <div>
        <div class="contact-label">Contact us anytime on</div>
        <div class="contact-number">0700 4418 263</div>
      </div>
    </div>
  </header>

  <nav class="main-nav">
    <ul>
      <li>Home</li>
      <li>About us</li>
      <li>Sell your property fast</li>
      <li>Rent your property fast</li>
      <li>The 5 easy steps</li>
      <li>Contact us</li>
    </ul>
  </nav>

  <section class="hero">
    <div class="hero-photo" role="img" aria-label="Blurred photo of a white suburban house with a sale board in the front garden"></div>

    <svg class="steps-path" width="100" height="260" viewBox="0 0 100 260" style="left:205px;top:55px;position:absolute">
      <path d="M5 0 C60 20 100 70 120 90" fill="none" stroke="#333" stroke-width="1" stroke-dasharray="3 3"/>
      <path d="M118 140 C60 160 40 200 80 240" fill="none" stroke="#333" stroke-width="1" stroke-dasharray="3 3"/>
    </svg>

    <div class="steps">
      <div class="step" style="top:0"><div class="step-icon"><svg viewBox="0 0 20 20"><rect x="4" y="2" width="12" height="16" rx="1" fill="var(--red)"/><circle cx="10" cy="8" r="2" fill="#fff"/><rect x="7" y="11" width="6" height="2" fill="#fff"/></svg></div><span class="step-label">Contact &nbsp;us</span></div>
      <div class="step" style="top:57px"><div class="step-icon"><svg viewBox="0 0 20 20"><path d="M3 9 L9 3 H17 V11 L11 17 Z" fill="var(--red)"/><circle cx="14" cy="6" r="1.5" fill="#fff"/></svg></div><span class="step-label">Free &nbsp;consultation</span></div>
      <div class="step" style="top:114px"><div class="step-icon"><svg viewBox="0 0 20 20"><circle cx="10" cy="8" r="6" fill="var(--red)"/><path d="M6 12 L5 19 L10 16 L15 19 L14 12Z" fill="var(--red)"/></svg></div><span class="step-label">Guranteed &nbsp;offer</span></div>
      <div class="step" style="top:171px"><div class="step-icon"><svg viewBox="0 0 20 20"><path d="M4 2 H12 L16 6 V18 H4Z" fill="none" stroke="var(--red)" stroke-width="1.5"/><path d="M7 10 H13 M7 13 H13" stroke="var(--red)" stroke-width="1.2"/></svg></div><span class="step-label">Legal &nbsp;stuff</span></div>
      <div class="step" style="top:228px"><div class="step-icon"><svg viewBox="0 0 20 20"><path d="M2 8 L10 3 L18 8Z" fill="var(--red)"/><rect x="3" y="9" width="14" height="8" fill="none" stroke="var(--red)" stroke-width="1.5"/><path d="M7 9 V17 M10 9 V17 M13 9 V17" stroke="var(--red)" stroke-width="1.2"/></svg></div><span class="step-label">Completion &nbsp;money in bank</span></div>
    </div>

    <div class="steps-title">
      <div class="the">THE</div>
      <div class="steps-num">5</div>
      <div class="easy">EASY</div>
      <div class="steps-word">STEPS</div>
    </div>

    <form class="valuation">
      <div class="valuation-inner">
        <div class="valuation-head">
          <svg width="16" height="11" viewBox="0 0 16 11"><rect width="16" height="11" fill="#fff"/><path d="M0 0 L8 6 L16 0" fill="none" stroke="var(--red)" stroke-width="1.5"/></svg>
          Request your free valuation
        </div>
        <div class="field" style="left:12px;top:43px;width:268px">Name</div>
        <div class="field" style="left:12px;top:80px;width:127px">Email</div>
        <div class="field" style="left:152px;top:80px;width:128px">Phone</div>
        <div class="field" style="left:12px;top:117px;width:268px">Property address</div>
        <div class="field" style="left:12px;top:154px;width:268px;height:47px">Message (optional)</div>
        <div class="submit">SUBMIT</div>
      </div>
    </form>
  </section>

  <section class="welcome">
    <h1>Welcome to<span>Juniper Estates</span></h1>
    <div class="welcome-text">
      <p>We are a family run business that ethically purchase, rent and manage property. This is often to remove people from stressful situations and help &nbsp;them solve &nbsp;their property problems.</p>
      <p>We pride ourselves on a friendly approachable style and treat each person uniquely. We aim to get to know you and for you to get to know our small team ersonally. We try, within reason, &nbsp;for you to &nbsp;deal in the &nbsp;majority with the same team member throughout the process. We are based and live in Bristol.</p>
    </div>
    <div class="welcome-photo" role="img" aria-label="Photo of a smiling family standing in front of their house and garden"></div>
  </section>

  <section class="help">
    <h2 class="section-title">Who can we help?</h2>
    <ul class="tick-list" style="left:108px;top:52px"><li>How to stop repossession</li><li>Divorce &nbsp;or separation</li><li>Financial problems</li></ul>
    <ul class="tick-list" style="left:242px;top:52px"><li>Don't like estate agents?</li><li>Property needing work</li><li>Retiring &nbsp;landlords</li></ul>
    <ul class="tick-list" style="left:381px;top:52px"><li>Negative equity</li><li>Opportunity not to be missed!!</li><li>Guaranteed rent scheme</li></ul>
    <ul class="tick-list" style="left:529px;top:52px"><li>Inherited property</li><li>Chain Collapse</li><li>Tenanted Property</li></ul>
    <ul class="tick-list" style="left:662px;top:52px"><li>Ill health</li><li>Relocating</li></ul>
  </section>

  <section class="special">
    <h2 class="section-title">We are a local family run property<br>business who specialize in</h2>
    <ul class="tick-list" style="left:96px;top:67px"><li>Buying properties quickly</li><li>Finding creative solutions to your property problems</li><li>Property rental management</li></ul>
    <ul class="tick-list" style="left:357px;top:67px;width:220px"><li>STOPPING repossessions</li><li>Lettings to professional and student tenants</li><li>Guaranteed rent and management schemes for landlords</li></ul>
    <ul class="tick-list" style="left:600px;top:67px"><li>Motivated sellers</li><li>Chain fixing</li><li>Negative equity problems</li></ul>
  </section>

  <section class="badges" aria-label="Accreditations">
    <div class="badge" style="left:96px;top:25px;width:177px;height:40px;background:#4b2a6a;border-radius:4px"></div>
    <div class="badge-divider" style="left:329px"></div>
    <div class="badge" style="left:380px;top:9px;width:53px;height:72px;background:#1a9aa6;border-radius:3px"></div>
    <div class="badge-divider" style="left:501px"></div>
    <div class="badge" style="left:563px;top:19px;width:155px;height:53px;background:#1b3a6b"></div>
  </section>

  <footer class="site-footer">
    <div class="footer-brand"><span class="brand-dot"></span><span class="brand-name">Juniper Estates</span></div>
    <ul class="footer-nav">
      <li>Home</li><li>About us</li><li>Sell your property fast</li><li>Rent your property fast</li><li>The 5 easy steps</li><li>Contact us</li>
    </ul>
    <div class="social"><span></span><span></span></div>
    <div class="copyright">© 2014 Juniper Estates Limited. Reg No 1234567</div>
  </footer>

</div>
</body>
</html>
```